Create a Graphic About YOURSELF and PixelHarbor

PixelHarbor would like you (designers) to create an awesome graphic to promote YOURSELF and your profile on PixelHarbor!

Your graphic should communicate your name, your services and should mention PixelHarbor.

The design should be perfect for sharing on Chatterly. Here's an example of what we'd like http://blog.pixelharbor-example.ca/article/333/pixelharbor-launches-3000-hire-me-social-design-contest

Once you submitted your design, we'd love you to share the design ('advertisement') and promote yourself and PixelHarbor to your friends and potential customers. So make your submissions great and get your friends to vote for your design by 'Liking' it on Chatterly!

Prizes:
$1500 - "PixelHarbor Community" prize awarded to the designer with the most Chatterly 'Likes'
5 x $50 for the next 5 'most liked' designs on Chatterly

$1000 - "Hire Me" prize awarded to the designer who receives the most client invites
5 x $50 for the next 5 'most invited' designers

In summary, this is a great opportunity for you to increase your exposure to PixelHarbor customers and win cash prizes. Show off your design skills and get hired by PixelHarbor customers from around the world!

Target Market(s)

Fans, friends and customers of YOU

Industry/Entity Type

Cash

Requirements
Must have
• 1) Include your PixelHarbor user name on the graphic so customers can find you in the PixelHarbor Designer Directory
2) Include the tagline "Hire Me on PixelHarbor.com!" in your graphic design.
3) Share your design's URL on our Chatterly wall at http://chatterly-example.com/pixelharbor and get your friends to 'like' your design.
Nice to have
• 1) Include a tagline that expresses your design approach/philosophy
2) Artwork dimensions: 403 x 403 px
3) You can submit more than 1 design!
Should not have
• You must own the copyright of any images you use including stock imagery.

```html
<!DOCTYPE html>
<html lang="en">
<head>
<meta charset="utf-8">
<title>OPENFORMLAB – Hire me on PixelHarbor.com</title>
<link rel="stylesheet" href="https://fonts.googleapis.com/css2?family=Josefin+Sans:wght@400;600;700&family=Arimo:wght@400&display=swap">
<style>
  :root {
    --red-bright: #f0260e;
    --red-mid: #b3130a;
    --red-deep: #6e0706;
    --white: #ffffff;
    --wave-tone: rgba(255, 215, 205, 0.28);
    --arrow-tone: rgba(255, 255, 255, 0.55);
  }
  * { margin: 0; padding: 0; box-sizing: border-box; }
  html, body { width: 1200px; height: 1200px; overflow: hidden; }
  body { background: var(--red-deep); }
  .poster {
    position: relative;
    width: 1200px;
    height: 1200px;
    overflow: hidden;
    background: radial-gradient(circle at 0% 0%, var(--red-bright) 0%, var(--red-mid) 45%, var(--red-deep) 100%);
    color: var(--white);
  }
  .wave-ribbon {
    position: absolute;
    left: 0;
    top: 300px;
    width: 1200px;
    height: 470px;
    border-radius: 50% / 40%;
    background: radial-gradient(ellipse at 50% 50%, var(--wave-tone) 0%, rgba(255, 215, 205, 0.12) 55%, rgba(255, 215, 205, 0) 75%);
  }
  .keyword {
    position: absolute;
    font-family: "Arimo", Arial, sans-serif;
    font-size: 27px;
    line-height: 1;
    color: var(--white);
  }
  .keyword--idea { left: 194px; top: 372px; }
  .keyword--different { left: 958px; top: 437px; }
  .keyword--experience { left: 842px; top: 624px; }
  .keyword--creativity { left: 318px; top: 685px; }
  .designer-name {
    position: absolute;
    left: 194px;
    top: 530px;
    font-family: "Josefin Sans", sans-serif;
    font-weight: 700;
    font-size: 98px;
    line-height: 1;
    letter-spacing: 1px;
    color: var(--white);
    white-space: nowrap;
  }
  .speed-arrow {
    position: absolute;
    left: 0;
    top: 952px;
    width: 450px;
    height: 126px;
    background: linear-gradient(90deg, var(--arrow-tone) 0%, rgba(255, 255, 255, 0.35) 100%);
  }
  .hire-line {
    position: absolute;
    right: 58px;
    top: 980px;
    font-family: "Josefin Sans", sans-serif;
    font-weight: 400;
    font-size: 68px;
    line-height: 1;
    color: var(--white);
  }
  .hire-line strong { font-weight: 700; }
  .site-address {
    position: absolute;
    right: 54px;
    top: 1056px;
    font-family: "Josefin Sans", sans-serif;
    font-weight: 600;
    font-size: 88px;
    line-height: 1;
    color: var(--white);
  }
</style>
</head>
<body>
  <main class="poster">
    <div class="wave-ribbon" role="img" aria-label="Flowing ribbon of fine wavy contour lines crossing the poster"></div>

    <span class="keyword keyword--idea">idea</span>
    <span class="keyword keyword--different">different</span>
    <h1 class="designer-name">OPENFORMLAB</h1>
    <span class="keyword keyword--experience">experience</span>
    <span class="keyword keyword--creativity">creativity</span>

    <div class="speed-arrow" role="img" aria-label="Decorative white striped arrow pointing right toward the tagline"></div>

    <p class="hire-line">Hire<strong>me</strong>on</p>
    <p class="site-address">PixelHarbor.com</p>
  </main>
</body>
</html>
```